Luminously Grounded Vitality

We want to design a business card that is modern and appealing for an innovative psychedelic telemedicine company that provides at-home ketamine-assisted therapy along with wellness, longevity, and anti-aging medicines. We want to use our deep purple and white plus other colors you can find on our website. We don't have any strict brand guidelines yet so feel free to get creative. We want a very professional, but technology first modern design that will instill trust, peace, calm, but also be attractive to investors in the healthcare and SaaS space.

```html
<!DOCTYPE html>
<html lang="en">
<head>
<meta charset="utf-8">
<title>Luminously Grounded Vitality – Business Card</title>
<link rel="stylesheet" href="https://fonts.googleapis.com/css2?family=Lato:wght@300;400;700&family=Montserrat:wght@600;700&display=swap">
<style>
  :root {
    --bg: #2c2e33;
    --orchid: #b46fa4;
    --indigo: #6d51a8;
    --white: #ffffff;
    --ink: #4a4a4f;
    --shadow: rgba(0, 0, 0, 0.45);
  }
  * { box-sizing: border-box; margin: 0; padding: 0; }
  html, body {
    width: 1200px;
    height: 952px;
    overflow: hidden;
    background: var(--bg);
  }
  .canvas {
    width: 1200px;
    height: 952px;
    display: flex;
    align-items: center;
    justify-content: center;
    gap: 40px;
  }
  .card {
    position: relative;
    width: 540px;
    height: 309px;
    overflow: hidden;
    box-shadow: 0 14px 30px var(--shadow);
  }

  /* Front */
  .card-front { background: var(--white); }
  .brand {
    position: absolute;
    left: 40px;
    top: 44px;
    display: flex;
    align-items: center;
    gap: 10px;
  }
  .brand-dot {
    width: 14px;
    height: 14px;
    border-radius: 50%;
    background: var(--indigo);
  }
  .brand-name {
    font-family: "Lato", sans-serif;
    font-weight: 400;
    font-size: 19px;
    color: var(--orchid);
    letter-spacing: 0.2px;
  }
  .address {
    position: absolute;
    left: 40px;
    top: 96px;
    display: flex;
    gap: 8px;
    font-family: "Lato", sans-serif;
    font-size: 10.5px;
    line-height: 1.35;
    color: var(--ink);
  }
  .contact-band {
    position: absolute;
    left: 0;
    top: 134px;
    width: 270px;
    height: 104px;
  }
  .contact-list {
    position: absolute;
    left: 40px;
    top: 146px;
    list-style: none;
    font-family: "Lato", sans-serif;
    font-size: 10.5px;
    color: var(--white);
  }
  .contact-list li {
    display: flex;
    align-items: center;
    gap: 8px;
    height: 24px;
  }
  .icon {
    width: 14px;
    height: 14px;
    flex: none;
  }
  .address .icon { margin-top: 1px; }
  .person {
    position: absolute;
    right: 40px;
    top: 124px;
    text-align: right;
  }
  .person-name {
    font-family: "Montserrat", sans-serif;
    font-weight: 600;
    font-size: 15px;
    letter-spacing: 0.5px;
    color: var(--indigo);
  }
  .person-name .surname { font-weight: 700; color: var(--orchid); }
  .person-title {
    margin-top: 4px;
    font-family: "Lato", sans-serif;
    font-size: 12px;
    color: var(--ink);
    letter-spacing: 0.4px;
  }

  /* Back */
  .card-back {
    background: var(--orchid);
    display: flex;
    align-items: center;
    justify-content: flex-end;
    padding-right: 44px;
  }
  .back-name {
    font-family: "Lato", sans-serif;
    font-weight: 400;
    font-size: 26px;
    color: var(--white);
    letter-spacing: 0.3px;
  }
</style>
</head>
<body>
<main class="canvas">

  <section class="card card-front" aria-label="Business card front">
    <div class="brand">
      <span class="brand-dot"></span>
      <span class="brand-name">Luminously Grounded Vitality</span>
    </div>

    <div class="address">
      <svg class="icon" viewBox="0 0 14 14" aria-hidden="true">
        <rect width="14" height="14" rx="2" fill="var(--indigo)"/>
        <path d="M7 2.5a3 3 0 0 1 3 3c0 2.2-3 5.8-3 5.8S4 7.7 4 5.5a3 3 0 0 1 3-3z" fill="var(--white)"/>
        <circle cx="7" cy="5.5" r="1.1" fill="var(--indigo)"/>
      </svg>
      <span>2175 Meridian Avenue<br>Portland, OR 97201</span>
    </div>

    <svg class="contact-band" viewBox="0 0 270 104" aria-hidden="true">
      <path d="M0 0 H270 V84 Q270 104 250 104 H0 Z" fill="var(--orchid)"/>
    </svg>

    <ul class="contact-list">
      <li>
        <svg class="icon" viewBox="0 0 14 14" aria-hidden="true">
          <rect width="14" height="14" rx="2" fill="var(--white)"/>
          <path d="M4.2 3.2l1.6-.4.9 2.2-1 .8a5.5 5.5 0 0 0 2.5 2.5l.8-1 2.2.9-.4 1.6c-3.8.3-6.9-2.8-6.6-6.6z" fill="var(--orchid)"/>
        </svg>
        <span>+00 987 654 32</span>
      </li>
      <li>
        <svg class="icon" viewBox="0 0 14 14" aria-hidden="true">
          <rect width="14" height="14" rx="2" fill="var(--white)"/>
          <rect x="3" y="4" width="8" height="6" fill="none" stroke="var(--orchid)" stroke-width="1.2"/>
          <path d="M3 4l4 3.2L11 4" fill="none" stroke="var(--orchid)" stroke-width="1.2"/>
        </svg>
        <span>hello@luminouslyvitality.com</span>
      </li>
      <li>
        <svg class="icon" viewBox="0 0 14 14" aria-hidden="true">
          <rect width="14" height="14" rx="2" fill="var(--white)"/>
          <path d="M4.5 3l5.5 4.2-2.4.4 1.4 2.8-1.1.5-1.4-2.8-2 1.5z" fill="var(--orchid)"/>
        </svg>
        <span>www.luminouslyvitality.com</span>
      </li>
    </ul>

    <div class="person">
      <p class="person-name">DANIEL R. <span class="surname">WHITMORE</span></p>
      <p class="person-title">Managing Director</p>
    </div>
  </section>

  <section class="card card-back" aria-label="Business card back">
    <p class="back-name">Luminously Grounded Vitality</p>
  </section>

</main>
</body>
</html>
```